1 Page for Computer Repair Website

Looking for a 1 page website with a design that compliments the business card and pamphlet that have already been made (attached files). It should look business professional and easy to read. Email and phone number should be somewhere near the top of the website, visible when the page loads. I don't want any forms for people to mess with. No "Contact Us" form or entering in email for newsletter. Customers will just be looking at this site to confirm we are professionals and have our business in order.

Target Market(s)

Home and small business

Industry/Entity Type

Computer Repair

Coding

Coded - Design and coding required

Number of Pages Required

1 page

Font styles to use
Other font styles liked:
• Helvetica variations used in pamphlet and card

Colors
0455a3
cfdeed
85abd2
3276b5
85cae6
ffffff

Requirements
Must have
• Compliment the pamphlet and business card in color choices and font use. Pleasing to the eye and easy to read through categories and text.
Should not have
• Forms. No "enter name and email here" or anything of the sort.

```html
<!DOCTYPE html>
<html lang="en">
<head>
<meta charset="utf-8">
<title>NexByte Computer Services</title>
<link rel="stylesheet" href="https://fonts.googleapis.com/css2?family=Open+Sans:wght@400;600;700;800&display=swap">
<style>
:root{
  --navy:#0a2a5c;
  --navy-deep:#07204a;
  --blue:#0455a3;
  --blue-mid:#3276b5;
  --blue-soft:#85abd2;
  --blue-sky:#85cae6;
  --blue-pale:#cfdeed;
  --grey-bg:#efefef;
  --text:#444a52;
  --heading:#1d2733;
  --white:#ffffff;
}
*{box-sizing:border-box;margin:0;padding:0}
html,body{width:1200px;height:2924px;overflow:hidden}
body{font-family:"Open Sans",Arial,sans-serif;color:var(--text);background:var(--white);position:relative}
a{color:inherit;text-decoration:none}

/* header */
.site-header{position:absolute;top:0;left:0;width:1200px;height:124px;background:var(--white)}
.brand{position:absolute;left:48px;top:26px;color:var(--navy)}
.brand-name{font-size:50px;font-weight:700;line-height:1;letter-spacing:1px}
.brand-sub{font-size:17px;font-weight:400;color:var(--blue-mid);margin-top:2px}
.contact-strip{position:absolute;right:0;top:0;width:480px;height:40px;background:var(--navy);border-bottom-left-radius:22px;display:flex;align-items:center;gap:50px;padding-left:70px;color:var(--white);font-size:14px}
.contact-strip span{display:flex;align-items:center;gap:10px}

/* nav */
.main-nav{position:absolute;top:124px;left:0;width:1200px;height:62px;background:var(--navy);display:flex;padding-left:60px}
.main-nav a{width:124px;text-align:center;line-height:62px;color:var(--white);font-size:13px;font-weight:600;letter-spacing:.5px}
.main-nav a.active{background:var(--blue-mid)}

/* hero */
.hero{position:absolute;top:186px;left:0;width:1200px;height:554px;overflow:hidden}
.hero-photo{position:absolute;inset:0;background:linear-gradient(120deg,#c8cdd3 0%,#9aa4ae 40%,#3d4651 75%,#22282f 100%)}
.hero-shade{position:absolute;left:0;bottom:0;width:1200px;height:300px;background:linear-gradient(180deg,rgba(7,32,74,0) 0%,rgba(7,32,74,.88) 55%)}
.hero-copy{position:absolute;left:60px;top:278px;width:560px;color:var(--white)}
.hero-copy h1{font-size:36px;font-weight:700;line-height:1.2}
.hero-copy h2{font-size:30px;font-weight:600;color:var(--blue-sky);line-height:1.2}
.hero-copy p{font-size:13px;line-height:1.6;margin-top:14px;color:#dbe5f1}
.btn{display:inline-block;background:var(--blue);color:var(--white);font-size:12px;font-weight:700;padding:0 22px;line-height:38px;letter-spacing:.5px}
.hero-copy .btn{margin-top:22px;background:var(--blue-mid)}
.slide-arrow{position:absolute;top:146px;width:34px;height:34px;border-radius:50%;background:rgba(255,255,255,.9);display:flex;align-items:center;justify-content:center}
.slide-arrow.prev{left:14px}.slide-arrow.next{right:14px}
.slide-dots{position:absolute;left:770px;top:492px;display:flex;gap:8px}
.slide-dots i{width:12px;height:12px;border-radius:50%;border:2px solid var(--white);display:block}
.slide-dots i.on{background:var(--white)}

/* headings */
.section-title{text-align:center;font-size:30px;font-weight:700;color:var(--heading)}
.section-title::after{content:"";display:block;width:60px;height:2px;background:var(--blue);margin:12px auto 0}

/* about */
.about{position:absolute;top:740px;left:0;width:1200px;height:270px;text-align:center;padding-top:44px}
.about p{width:900px;margin:26px auto 0;font-size:13px;line-height:1.7}
.about .btn{margin-top:24px;background:var(--navy)}

/* services */
.services{position:absolute;top:1010px;left:0;width:1200px;height:760px;background:var(--grey-bg);padding-top:54px}
.service-grid{position:absolute;top:140px;left:0;width:1200px}
.service{position:absolute;width:480px;height:130px}
.service .num{position:absolute;top:12px;width:92px;height:92px;border-radius:50%;border:3px solid var(--blue-soft);background:var(--white);color:var(--navy);font-size:34px;font-weight:700;display:flex;align-items:center;justify-content:center}
.service h3{font-size:16px;font-weight:700;color:var(--heading)}
.service p{font-size:11.5px;line-height:1.55;margin-top:6px}
.service .more{display:block;font-size:10px;font-weight:800;color:var(--navy);margin-top:4px}
.service.left{left:140px;text-align:right}
.service.left .num{right:0}
.service.left .body{position:absolute;right:116px;top:0;width:320px}
.service.right{left:654px}
.service.right .num{left:0}
.service.right .body{position:absolute;left:116px;top:0;width:320px}

/* why */
.why{position:absolute;top:1770px;left:0;width:1200px;height:410px;padding-top:108px}
.why-photo{position:absolute;left:50px;top:190px;width:480px;height:200px;background:linear-gradient(135deg,#5d7ea8 0%,#a8bdd6 45%,#d9e2ec 100%)}
.why-list{position:absolute;left:580px;top:186px;width:560px;list-style:none}
.why-list li{position:relative;padding-left:20px;font-size:11.5px;line-height:1.55;margin-bottom:12px}
.why-list li::before{content:"";position:absolute;left:2px;top:6px;width:6px;height:6px;border-radius:50%;background:var(--navy)}

/* help */
.help{position:absolute;top:2180px;left:0;width:1200px;height:380px;background:var(--navy);color:var(--white);text-align:center;padding-top:80px}
.help h2{font-size:28px;font-weight:700}
.help-items{display:flex;justify-content:center;gap:180px;margin-top:48px}
.help-item{width:110px}
.help-icon{width:98px;height:98px;border-radius:50%;background:var(--white);margin:0 auto;display:flex;align-items:center;justify-content:center}
.help-item span{display:block;margin-top:24px;font-size:15px;font-weight:700;letter-spacing:.3px;white-space:nowrap;margin-left:-40px;margin-right:-40px}

/* footer */
.site-footer{position:absolute;top:2560px;left:0;width:1200px;height:280px;background:#f4f5f7}
.site-footer .brand{left:64px;top:62px}
.footer-col{position:absolute;top:60px}
.footer-col h4{font-size:15px;font-weight:700;color:var(--heading);margin-bottom:12px}
.footer-col ul{list-style:none}
.footer-col li{font-size:11px;line-height:2;padding-left:12px;position:relative}
.footer-col li::before{content:"›";position:absolute;left:0;color:var(--navy);font-weight:700}
.col-links{left:400px}.col-cats{left:680px}.col-nav{left:968px}

.bottom-bar{position:absolute;top:2840px;left:0;width:1200px;height:84px;background:var(--navy-deep);color:#c7d3e4;font-size:11px;text-align:center;line-height:84px}
</style>
</head>
<body>

<header class="site-header">
  <div class="brand">
    <div class="brand-name">NEXBYTE</div>
    <div class="brand-sub">Computer Services</div>
  </div>
  <div class="contact-strip">
    <span>help@nexbyte-repair.com</span>
    <span>
      <svg width="14" height="14" viewBox="0 0 24 24" fill="#fff"><path d="M6.6 10.8a15.1 15.1 0 0 0 6.6 6.6l2.2-2.2a1 1 0 0 1 1-.25 11.4 11.4 0 0 0 3.6.57 1 1 0 0 1 1 1V20a1 1 0 0 1-1 1A17 17 0 0 1 3 4a1 1 0 0 1 1-1h3.5a1 1 0 0 1 1 1c0 1.25.2 2.45.57 3.57a1 1 0 0 1-.25 1z"/></svg>
      (555) 014-2290
    </span>
  </div>
</header>

<nav class="main-nav">
  <a class="active" href="#">HOME</a>
  <a href="#">ABOUT US</a>
  <a href="#">SERVICE</a>
  <a href="#">FAQS</a>
  <a href="#">NEWS</a>
  <a href="#">CONTACT US</a>
</nav>

<section class="hero">
  <div class="hero-photo" role="img" aria-label="Technician repairing an open desktop computer tower, with a blue swoosh graphic across it"></div>
  <div class="hero-shade"></div>
  <div class="slide-arrow prev"><svg width="12" height="12" viewBox="0 0 12 12"><path d="M8 1 3 6l5 5" stroke="#0a2a5c" stroke-width="2" fill="none"/></svg></div>
  <div class="slide-arrow next"><svg width="12" height="12" viewBox="0 0 12 12"><path d="M4 1l5 5-5 5" stroke="#0a2a5c" stroke-width="2" fill="none"/></svg></div>
  <div class="hero-copy">
    <h1>Any Computer Problems?</h1>
    <h2>Receive Instant Service!</h2>
    <p>Fast, friendly repair for laptops, desktops and home networks. Our certified technicians diagnose the problem, explain your options in plain language and get you back to work quickly.</p>
    <a class="btn" href="#">READ MORE</a>
  </div>
  <div class="slide-dots"><i class="on"></i><i></i><i></i><i></i></div>
</section>

<section class="about">
  <h2 class="section-title">About Us</h2>
  <p>We are a local computer repair team serving homes and small businesses across the region. From a slow laptop to a failed office server, we handle every job with care, clear pricing and honest advice. Our technicians are certified, insured and trained on all major platforms, and every repair is backed by a ninety-day workmanship guarantee. We keep you informed from drop-off to pickup, so there are never any surprises on the final invoice.</p>
  <a class="btn" href="#">READ MORE</a>
</section>

<section class="services">
  <h2 class="section-title">OUR SERVICE</h2>
  <div class="service-grid">
    <div class="service left" style="top:0">
      <div class="body"><h3>Malware Removal</h3><p>We remove viruses, spyware and ransomware, then harden your system so the same threats cannot return.</p><a class="more" href="#">READ MORE ›</a></div>
      <div class="num">01</div>
    </div>
    <div class="service right" style="top:0">
      <div class="num">02</div>
      <div class="body"><h3>PC/Laptop Hardware Repair</h3><p>Screens, keyboards, batteries, fans and motherboards replaced with quality parts and tested before your device goes home.</p><a class="more" href="#">READ MORE ›</a></div>
    </div>
    <div class="service left" style="top:160px">
      <div class="body"><h3>Hard/Software Upgrades</h3><p>Add memory, swap in a fast SSD or move to the latest operating system without losing your settings.</p><a class="more" href="#">READ MORE ›</a></div>
      <div class="num">03</div>
    </div>
    <div class="service right" style="top:160px">
      <div class="num">04</div>
      <div class="body"><h3>Date Migration</h3><p>Move files, email and programs from an old machine to a new one safely, with nothing left behind.</p><a class="more" href="#">READ MORE ›</a></div>
    </div>
    <div class="service left" style="top:320px">
      <div class="body"><h3>Date Resue</h3><p>Deleted files or a failing drive? We recover photos, documents and records from disks, cards and USB sticks.</p><a class="more" href="#">READ MORE ›</a></div>
      <div class="num">05</div>
    </div>
    <div class="service right" style="top:320px">
      <div class="num">06</div>
      <div class="body"><h3>In-Home Installation</h3><p>We set up computers, printers and Wi-Fi at your home or office and make sure everything works together.</p><a class="more" href="#">READ MORE ›</a></div>
    </div>
    <div class="service left" style="top:480px">
      <div class="body"><h3>Clean/tune ups</h3><p>A thorough cleanup of dust, startup clutter and unused programs to bring back the speed you remember.</p><a class="more" href="#">READ MORE ›</a></div>
      <div class="num">07</div>
    </div>
    <div class="service right" style="top:480px">
      <div class="num">08</div>
      <div class="body"><h3>Remote Support</h3><p>Quick fixes over a secure remote connection, so many problems are solved without a visit or a drive.</p><a class="more" href="#">READ MORE ›</a></div>
    </div>
  </div>
</section>

<section class="why">
  <h2 class="section-title">Why Choose Us</h2>
  <div class="why-photo" role="img" aria-label="Technicians working with network equipment in a server room"></div>
  <ul class="why-list">
    <li>Certified technicians with years of hands-on experience repairing every major brand of desktop and laptop.</li>
    <li>Clear, upfront quotes before any work begins, so you always know what you will pay.</li>
    <li>Fast turnaround on most repairs, with many jobs finished the same or next business day.</li>
    <li>Ninety-day guarantee on parts and labour for complete peace of mind after every repair.</li>
    <li>Friendly service for homes and small businesses, with on-site visits available throughout the area.</li>
  </ul>
</section>

<section class="help">
  <h2>Just in Case You Need Any Help</h2>
  <div class="help-items">
    <div class="help-item">
      <div class="help-icon"><svg width="44" height="44" viewBox="0 0 24 24"><rect x="2" y="5" width="20" height="14" rx="1.5" fill="#0a2a5c"/><path d="M3 6l9 7 9-7" stroke="#fff" stroke-width="1.6" fill="none"/></svg></div>
      <span>EMAIL SUPPORT</span>
    </div>
    <div class="help-item">
      <div class="help-icon"><svg width="44" height="44" viewBox="0 0 24 24"><rect x="6" y="2" width="12" height="20" rx="2" fill="none" stroke="#0a2a5c" stroke-width="2"/><circle cx="12" cy="18.5" r="1.2" fill="#0a2a5c"/></svg></div>
      <span>FREE PHONE</span>
    </div>
    <div class="help-item">
      <div class="help-icon"><svg width="44" height="44" viewBox="0 0 24 24"><path d="M21 6.5a5 5 0 0 1-6.6 4.7L6 19.6a2 2 0 0 1-2.8-2.8l8.4-8.4A5 5 0 0 1 17.5 3l-3 3 .5 3 3 .5z" fill="#0a2a5c"/></svg></div>
      <span>24/7 SUPPORT</span>
    </div>
    <div class="help-item">
      <div class="help-icon"><svg width="44" height="44" viewBox="0 0 24 24"><path d="M8.5 9a3.5 3.5 0 1 1 5 3.2c-1 .5-1.5 1.2-1.5 2.3v.8" stroke="#0a2a5c" stroke-width="2.4" fill="none" stroke-linecap="round"/><circle cx="12" cy="19.5" r="1.5" fill="#0a2a5c"/></svg></div>
      <span>FAQ</span>
    </div>
  </div>
</section>

<footer class="site-footer">
  <div class="brand">
    <div class="brand-name">NEXBYTE</div>
    <div class="brand-sub">Computer Services</div>
  </div>
  <div class="footer-col col-links">
    <h4>Important Links</h4>
    <ul><li>Affiliate Program</li><li>General Questions</li><li>Newsletter</li><li>Careers</li></ul>
  </div>
  <div class="footer-col col-cats">
    <h4>Categories</h4>
    <ul><li>Data Recovery Services</li><li>Certified Technicians</li><li>On-site Home Service</li><li>Remote Diagnostics</li></ul>
  </div>
  <div class="footer-col col-nav">
    <h4>Navigation</h4>
    <ul><li>About Us</li><li>Services</li><li>FAQs</li><li>News</li><li>Contact Us</li></ul>
  </div>
</footer>

<div class="bottom-bar">
  Copyright 2016 NexByte Computer Services. All Rights Reserved.
</div>

</body>
</html>
```